Business Card Design Project

I need a business card designed for TalePorter, a website which has people share their fictional story ideas with others. The business cards should incorporate the websites's logo, which can be found at www.taleporter-demo.net .

Target Market(s)

These will be primarily used in business development activities, not given to customers. It therefore needs to have a clean, professional appearance, and yet communicate what the company is trying to achieve as a bold startup.

Industry/Entity Type

Business

```html
<!DOCTYPE html>
<html lang="en">
<head>
<meta charset="utf-8">
<title>TalePorter Business Cards</title>
<link rel="stylesheet" href="https://fonts.googleapis.com/css2?family=Montserrat:wght@500&family=Open+Sans:wght@400;600&display=swap">
<style>
  :root {
    --backdrop: #e9eaea;
    --navy: #1f4466;
    --navy-circle: #6a7c99;
    --pale: #cddff0;
    --pale-circle: #b5c6de;
    --white: #ffffff;
  }
  html, body {
    margin: 0;
    padding: 0;
    width: 1200px;
    height: 1000px;
    overflow: hidden;
    background: var(--backdrop);
  }
  .canvas {
    position: relative;
    width: 1200px;
    height: 1000px;
    display: flex;
    flex-direction: column;
    align-items: center;
    justify-content: center;
    gap: 60px;
  }
  .card {
    width: 540px;
    height: 310px;
    display: block;
  }
  .wordmark-front {
    font-family: "Montserrat", sans-serif;
    font-weight: 500;
    font-size: 34px;
    fill: var(--white);
  }
  .wordmark-back {
    font-family: "Open Sans", sans-serif;
    font-weight: 600;
    font-size: 24px;
    fill: var(--navy);
  }
  .web-address {
    font-family: "Open Sans", sans-serif;
    font-weight: 400;
    font-size: 21px;
    fill: var(--pale);
  }
</style>
</head>
<body>
  <main class="canvas">
    <svg class="card card-front" viewBox="0 0 540 310" aria-label="Business card front">
      <defs>
        <clipPath id="front-clip"><rect width="540" height="310"/></clipPath>
      </defs>
      <g clip-path="url(#front-clip)">
        <rect class="card-base" width="540" height="310" fill="var(--navy)"/>
        <circle class="accent-circle" cx="462" cy="92" r="112" fill="var(--navy-circle)"/>
      </g>
      <circle class="brand-dot" cx="68" cy="153" r="27" fill="var(--pale)"/>
      <text class="wordmark-front" x="108" y="165">TalePorter</text>
    </svg>

    <svg class="card card-back" viewBox="0 0 540 310" aria-label="Business card back">
      <defs>
        <clipPath id="back-clip"><rect width="540" height="310"/></clipPath>
      </defs>
      <g clip-path="url(#back-clip)">
        <rect class="card-base" width="540" height="310" fill="var(--pale)"/>
        <circle class="accent-circle" cx="275" cy="190" r="155" fill="var(--pale-circle)"/>
        <path class="footer-band" d="M190 310 C 250 250, 380 225, 540 250 L540 310 Z" fill="var(--navy)"/>
      </g>
      <circle class="brand-dot" cx="36" cy="36" r="22" fill="var(--navy)"/>
      <text class="wordmark-back" x="70" y="45">TalePorter</text>
      <text class="web-address" x="522" y="292" text-anchor="end">www.taleporter-demo.net</text>
    </svg>
  </main>
</body>
</html>
```